VEXMORA, INC. BUSINESS CARD REDESIGN

Attached is an example business card. Name, Title, Address, Contact Information, logo and social media icons are ALL required to be designed into the card. The logo can be modified. An exact replica (or few modifications) of the existing design will be rejected.

Card can either have a blue or white background. Blues and any complimentary color of social media logos that are included on the card.

An example is attached/provided but should not be merely copied or slightly modified.

This should be a new, innovative design relative to the general concept of the existing business card.

Reason: This project has been updated; please utilize the original logo as much as possible. Also because of the high quality of most of the submissions the company requires additional time to reach out with feedback to the top designers for editing and re-submission to determine the finalist. Thank you.

Target Market(s)

B2B (business to business), Television News Stations, Broadcasting, Radio, Magazine and Newspaper Organizations.

Industry/Entity Type

Media

Contact Information for Business Card

Example attached. Company name with exisiting logo (can be altered/edited) in blue (similar to quorble/lintavo blue, but brighter and/or bolder).

Optional two sided card so that just the "VEXMORA" logo is on the front side of the card with contact information on the back side.

Logo Text

VEXMORA

Font styles to use
Sans Serif
Other font styles liked:
• ubuntu, ubuntu bold etc...or similar clean fonts that look great on mobile. Open to use of Google Fonts.

Requirements
Must have
• Must have the following branding integrated into the design (not in any specefic order or verbatim):
• VEXMORA, INC.
• Milo Brandt CEO & Founder
• 83 Wrenfield Nashville, TN 37210
• mobile: 615.555.0142
• milo@vexmora-mail.test
• https://vexmora-mail.test
• Must also include brand assests (e.g. official logos) of QUORBLE, LINTAVO, MARQEEN, SOLLIVAR, DREVONIX, and KELMITRU
• A clean logo only on the front side is requested (blue or white background). The front side can incorporate the social media icons listed in the brief if designer chooses.
Nice to have
• Card can either have a blue or white background. Blues and any complimentary color of social media logos that are included on the card.
• The card can be double sided so that the logo is on front and contact information is professionally displayed on the back. Not necessarily a requirement but a double-sided design will receive a higher preference.
• An example is attached/provided but should not be merely copied or slightly modified.
• This should be a new, innovative design relative to the general concept of the existing business card.
• Also the brand name with the TM trademark after: for example, Vexmora™
• This (the tm) should be added only after a standalone use of just the word VEXMORA or Vexmora™ AND not Vexmora™, Inc., included in the URL or email address obviously. Thanks :)
Should not have
• Should not have the text spelling of Lintavo, Drevonix, Sollivar, Kelmitru, etc...with the exception of "Marqeen" as it is the approved logo to be integrated.

```html
<!DOCTYPE html>
<html lang="en">
<head>
<meta charset="utf-8">
<title>Vexmora™ Business Card</title>
<link href="https://fonts.googleapis.com/css2?family=Open+Sans:wght@400;600&display=swap" rel="stylesheet">
<style>
  :root {
    --brand-blue: #1a72aa;
    --panel-blue: #1b72a9;
    --ribbon-red: #cf2027;
    --icon-red: #d6232a;
    --paper: #ffffff;
    --backdrop: #cfcfcf;
    --marqeen: #e3322f;
    --lintavo: #2d3a8f;
    --drevonix: #e1306c;
    --quorble: #27a6e1;
    --sollivar: #cc1f2d;
    --kelmitru: #f4d81a;
  }
  * { box-sizing: border-box; margin: 0; padding: 0; }
  html, body { width: 1200px; height: 1200px; overflow: hidden; }
  body {
    background: radial-gradient(circle at 80% 85%, #f2f2f2 0%, var(--backdrop) 45%, #b9b9b9 100%);
    font-family: "Open Sans", sans-serif;
    position: relative;
  }
  .card {
    position: absolute;
    width: 700px;
    height: 400px;
    background: var(--paper);
    box-shadow: 0 10px 28px rgba(0,0,0,0.22);
    overflow: hidden;
  }
  .card--contact { left: 140px; top: 60px; }
  .card--brand { left: 360px; top: 500px; }

  /* contact side */
  .blue-panel {
    position: absolute; inset: 0;
    background: var(--panel-blue);
    clip-path: polygon(46% 0, 100% 0, 100% 100%, 76% 100%);
  }
  .name-ribbon {
    position: absolute;
    left: 380px; top: 120px;
    width: 320px; height: 96px;
    background: var(--ribbon-red);
    color: #fff;
    padding: 14px 0 0 30px;
    box-shadow: -4px 6px 10px rgba(0,0,0,0.18);
  }
  .name-ribbon .person-name { font-size: 36px; font-weight: 600; letter-spacing: 0.5px; line-height: 1.1; white-space: nowrap; }
  .name-ribbon .person-title { font-size: 15px; letter-spacing: 6px; margin-top: 6px; white-space: nowrap; }

  .wordmark { display: flex; align-items: center; color: var(--brand-blue); white-space: nowrap; }
  .wordmark .mark-dot { border-radius: 50%; background: var(--brand-blue); flex: none; }
  .wordmark .tm { font-size: 0.32em; vertical-align: top; margin-left: 2px; }

  .wordmark--small { position: absolute; left: 50px; top: 90px; font-size: 44px; letter-spacing: 1px; }
  .wordmark--small .mark-dot { width: 56px; height: 56px; margin-right: 12px; }

  .contact-list { position: absolute; left: 60px; top: 250px; list-style: none; }
  .contact-list li {
    display: flex; align-items: center; gap: 12px;
    font-size: 14px; color: var(--brand-blue); margin-bottom: 9px; white-space: nowrap;
  }
  .contact-list svg { width: 18px; height: 18px; fill: var(--icon-red); flex: none; }

  /* brand side */
  .wordmark--large { position: absolute; left: 0; right: 0; top: 100px; justify-content: center; font-size: 72px; letter-spacing: 2px; }
  .wordmark--large .mark-dot { width: 92px; height: 92px; margin-right: 18px; }

  .social-row {
    position: absolute; left: 60px; right: 60px; bottom: 60px;
    display: flex; justify-content: space-between; list-style: none;
  }
  .social-row .network-dot { display: block; width: 56px; height: 56px; border-radius: 50%; }

  .wordmark--standalone { position: absolute; right: 120px; top: 1030px; font-size: 56px; letter-spacing: 1px; }
  .wordmark--standalone .mark-dot { width: 70px; height: 70px; margin-right: 14px; }
</style>
</head>
<body>

<section class="card card--contact" aria-label="Contact side">
  <div class="blue-panel"></div>
  <div class="name-ribbon">
    <div class="person-name">Milo Brandt</div>
    <div class="person-title">CEO &amp; Founder</div>
  </div>
  <div class="wordmark wordmark--small">
    <span class="mark-dot"></span><span>VEXMORA<span class="tm">™</span></span>
  </div>
  <ul class="contact-list">
    <li>
      <svg viewBox="0 0 24 24"><path d="M12 2a7 7 0 0 0-7 7c0 5 7 13 7 13s7-8 7-13a7 7 0 0 0-7-7zm0 9.5A2.5 2.5 0 1 1 12 6.5a2.5 2.5 0 0 1 0 5z"/></svg>
      83 Wrenfield Nashville, TN 37210
    </li>
    <li>
      <svg viewBox="0 0 24 24"><path d="M12 2a10 10 0 1 0 0 20 10 10 0 0 0 0-20zm6.9 9h-3a15 15 0 0 0-1.3-6A8 8 0 0 1 18.9 11zM12 4c.9 1.2 1.8 3.7 1.9 7h-3.8C10.2 7.7 11.1 5.2 12 4zM9.4 5a15 15 0 0 0-1.3 6h-3A8 8 0 0 1 9.4 5zM5.1 13h3a15 15 0 0 0 1.3 6A8 8 0 0 1 5.1 13zM12 20c-.9-1.2-1.8-3.7-1.9-7h3.8c-.1 3.3-1 5.8-1.9 7zm2.6-1a15 15 0 0 0 1.3-6h3a8 8 0 0 1-4.3 6z"/></svg>
      www.vexmora-mail.test
    </li>
    <li>
      <svg viewBox="0 0 24 24"><path d="M2 11 22 3l-6 18-4-7-10-3zm10 2 2.5 4.5L18 7l-6 6z"/></svg>
      milo@vexmora-mail.test
    </li>
    <li>
      <svg viewBox="0 0 24 24"><path d="M6.6 10.8a15 15 0 0 0 6.6 6.6l2.2-2.2a1 1 0 0 1 1-.25 11.4 11.4 0 0 0 3.6.57 1 1 0 0 1 1 1V20a1 1 0 0 1-1 1A17 17 0 0 1 3 4a1 1 0 0 1 1-1h3.5a1 1 0 0 1 1 1c0 1.25.2 2.45.57 3.57a1 1 0 0 1-.25 1z"/></svg>
      615.555.0142
    </li>
  </ul>
</section>

<section class="card card--brand" aria-label="Brand side">
  <div class="wordmark wordmark--large">
    <span class="mark-dot"></span><span>VEXMORA<span class="tm">™</span></span>
  </div>
  <ul class="social-row" aria-label="Social networks">
    <li aria-label="Marqeen"><span class="network-dot" style="background:var(--marqeen)"></span></li>
    <li aria-label="Lintavo"><span class="network-dot" style="background:var(--lintavo)"></span></li>
    <li aria-label="Drevonix"><span class="network-dot" style="background:var(--drevonix)"></span></li>
    <li aria-label="Quorble"><span class="network-dot" style="background:var(--quorble)"></span></li>
    <li aria-label="Sollivar"><span class="network-dot" style="background:var(--sollivar)"></span></li>
    <li aria-label="Kelmitru"><span class="network-dot" style="background:var(--kelmitru)"></span></li>
  </ul>
</section>

<div class="wordmark wordmark--standalone">
  <span class="mark-dot"></span><span>VEXMORA<span class="tm">™</span></span>
</div>

</body>
</html>
```